Powerpoint template design for Oil and Gas Investment Fund Pitchdeck

I need a template design for an oil and gas investment fund pitch deck. Design needs to be clean and have plenty of space for inserting graphics. Audience is high net worth individuals and corporate finance executives (private equity firms). We will need a title page with our logo and some oil& gas images (some included already) and the template for the internal pages. A rough example is attached. I would like to keep the current page dimensions because we have many financial charts we will want to add to the template pages. So the template will need to include title page, internal page, and a team page.

Target Market(s)

High etw worth individual investors and corporate finance professionals

Industry/Entity Type

Oil an dgas investment fund

Font styles to use
Serif

Requirements
Must have
• title page, interior page, team page

```html
<!DOCTYPE html>
<html lang="en">
<head>
<meta charset="utf-8">
<title>Halden Ridge Partners – Pitch Deck Template</title>
<link href="https://fonts.googleapis.com/css2?family=Crimson+Pro:wght@400;600;700&display=swap" rel="stylesheet">
<style>
:root{
  --stage:#d8d8d8;
  --paper:#ffffff;
  --ink:#000000;
  --text:#222222;
  --muted:#555555;
  --rule:#1a1a1a;
  --pill:#b5b5b5;
  --photo-sunset-a:#e8b48a;
  --photo-sunset-b:#4a4a52;
  --photo-field-a:#c9c2ae;
  --photo-field-b:#7d7866;
  --photo-rust-a:#c99a6a;
  --photo-rust-b:#3b2c22;
  --photo-amber-a:#d99b3c;
  --photo-amber-b:#3a2410;
  --portrait-a:#8a8d92;
  --portrait-b:#1f2226;
}
*{box-sizing:border-box;margin:0;padding:0}
html,body{width:1200px;height:2565px;overflow:hidden}
body{background:var(--stage);position:relative;font-family:"Crimson Pro",Georgia,serif;color:var(--text)}
.slide{position:absolute;width:545px;height:306px;background:var(--paper);overflow:hidden}
.slide--dark{background:var(--ink);color:#fff}
.col-left{left:47px}.col-right{left:614px}
.row-1{top:890px}.row-2{top:1222px}.row-3{top:1554px}.row-4{top:1886px}.row-5{top:2218px}
.slide svg.bg{position:absolute;left:0;top:0}
.notch{position:absolute;left:0;top:2px;width:0;height:0;border-top:28px solid transparent;border-bottom:28px solid transparent;border-left:26px solid var(--ink)}
.slide-title{position:absolute;left:34px;top:16px;font-size:22px;font-weight:600;color:var(--ink);line-height:1}
.mini-brand{position:absolute;right:16px;top:26px;font-size:6px;letter-spacing:1px;color:var(--ink);font-weight:600}
.footer-rule{position:absolute;left:32px;top:292px;width:470px;height:1px;background:var(--rule)}
.page-no{position:absolute;left:503px;top:283px;width:18px;height:18px;background:var(--ink);transform:rotate(45deg);border-radius:2px}
.page-no span{position:absolute;inset:0;transform:rotate(-45deg);color:#fff;font-size:7px;display:flex;align-items:center;justify-content:center}
.body-copy{position:absolute;font-size:9.4px;line-height:1.28;color:var(--text)}
.body-copy p{margin-bottom:10px}
.body-copy p.tight{margin-bottom:0}
.brand-name{font-weight:600;letter-spacing:2.4px;color:inherit;display:flex;align-items:center;gap:6px;white-space:nowrap}
.brand-name i{display:inline-block;width:10px;height:10px;background:currentColor}
.cover-brand{position:absolute;left:268px;top:186px;width:250px;justify-content:center;font-size:13px}
.cover-tagline{position:absolute;left:268px;top:227px;width:250px;text-align:center;font-size:12.4px;line-height:1.5;font-weight:600;color:var(--ink)}
.slide--dark .cover-tagline{font-weight:400;color:#fff}
.cover-pageno{position:absolute;left:446px;top:291px;font-size:7px;color:var(--ink)}
.placeholder{position:absolute;font-size:0}
.callout{position:absolute;left:250px;top:252px;width:238px;height:30px;background:var(--pill);border-radius:6px;font-size:9px;line-height:1.2;text-align:center;padding-top:3px;color:#222}
.intro{position:absolute;left:36px;top:70px;font-size:9px;line-height:1.3}
.team-member{position:absolute;top:140px;width:90px;text-align:center;transform:translateX(-50%)}
.team-member .name{font-size:8.2px;font-weight:600;color:var(--ink)}
.team-member .role{font-size:5.6px;font-style:italic;color:var(--muted);line-height:1.3;margin-top:3px}
.team-member .bio{font-size:5.6px;line-height:1.3;color:var(--muted);margin-top:3px}
.advisors-label{position:absolute;left:395px;top:46px;font-size:8px;letter-spacing:.5px}
.team-divider{position:absolute;left:318px;top:46px;width:1px;height:198px;background:var(--rule)}
.partner-strip{position:absolute;left:60px;top:252px;width:425px;height:30px;background:#fff;border-radius:8px;box-shadow:0 1px 6px rgba(0,0,0,.2);display:flex;align-items:center;justify-content:space-around;padding:0 16px}
.partner-badge{width:56px;height:12px;background:#9aa3b0;border-radius:2px}
.disclaimer-band{position:absolute;left:0;top:112px;width:545px;height:118px;background:var(--ink);color:#fff;font-size:9.6px;line-height:1.22;padding:15px 34px 0 37px}
.thanks-rule{position:absolute;left:27px;top:0;width:1px;height:282px;background:currentColor}
.thanks-brand{position:absolute;left:42px;top:98px;font-size:12px}
.thanks-title{position:absolute;left:39px;top:134px;font-size:25px;font-weight:700;line-height:1}
.thanks-copy{position:absolute;left:42px;top:186px;width:130px;font-size:9.4px;line-height:1.3;font-weight:400}
.social{position:absolute;left:20px;top:283px;display:flex;gap:8px}
.social span{width:12px;height:12px;border:1px solid currentColor;border-radius:50%}
</style>
</head>
<body>

<!-- Cover, light -->
<section class="slide col-left row-1">
  <svg class="bg" width="545" height="306" viewBox="0 0 545 306">
    <defs>
      <linearGradient id="g-sunset" x1="0" y1="0" x2="0" y2="1"><stop offset="0" stop-color="var(--photo-sunset-a)"/><stop offset="1" stop-color="var(--photo-sunset-b)"/></linearGradient>
      <linearGradient id="g-field" x1="0" y1="0" x2="0" y2="1"><stop offset="0" stop-color="var(--photo-field-a)"/><stop offset="1" stop-color="var(--photo-field-b)"/></linearGradient>
      <linearGradient id="g-rust" x1="0" y1="0" x2="0" y2="1"><stop offset="0" stop-color="var(--photo-rust-a)"/><stop offset="1" stop-color="var(--photo-rust-b)"/></linearGradient>
    </defs>
    <rect x="-58" y="-58" width="116" height="116" rx="12" transform="translate(165 5) rotate(45)" fill="#000"/>
    <rect x="-58" y="-58" width="116" height="116" rx="12" transform="translate(80 298) rotate(45)" fill="#000"/>
    <rect x="-58" y="-58" width="116" height="116" rx="12" transform="translate(560 -10) rotate(45)" fill="#000"/>
    <rect role="img" aria-label="Photo: offshore drilling rig at sunset" x="-58" y="-58" width="116" height="116" rx="12" transform="translate(80 95) rotate(45)" fill="url(#g-sunset)"/>
    <rect role="img" aria-label="Photo: drilling platform lit by low sun" x="-58" y="-58" width="116" height="116" rx="12" transform="translate(250 95) rotate(45)" fill="url(#g-sunset)"/>
    <rect role="img" aria-label="Photo: pumpjacks in a hazy oil field" x="-58" y="-58" width="116" height="116" rx="12" transform="translate(165 198) rotate(45)" fill="url(#g-field)"/>
    <rect role="img" aria-label="Photo: refinery towers" x="-58" y="-58" width="116" height="116" rx="12" transform="translate(460 92) rotate(45)" fill="url(#g-rust)"/>
  </svg>
  <div class="cover-brand brand-name" style="color:var(--ink)"><i></i>HALDEN RIDGE</div>
  <div class="cover-tagline">Consolidating profitable conventional<br>West Texas Oil &amp; Gas wells<br>into a high return investment fund</div>
  <div class="cover-pageno">1</div>
</section>

<!-- Cover, dark -->
<section class="slide slide--dark col-right row-1">
  <svg class="bg" width="545" height="306" viewBox="0 0 545 306">
    <defs>
      <linearGradient id="g-sunset2" x1="0" y1="0" x2="0" y2="1"><stop offset="0" stop-color="var(--photo-sunset-a)"/><stop offset="1" stop-color="var(--photo-sunset-b)"/></linearGradient>
      <linearGradient id="g-field2" x1="0" y1="0" x2="0" y2="1"><stop offset="0" stop-color="var(--photo-field-a)"/><stop offset="1" stop-color="var(--photo-field-b)"/></linearGradient>
      <linearGradient id="g-rust2" x1="0" y1="0" x2="0" y2="1"><stop offset="0" stop-color="var(--photo-rust-a)"/><stop offset="1" stop-color="var(--photo-rust-b)"/></linearGradient>
    </defs>
    <rect x="0" y="0" width="545" height="306" fill="#fff"/>
    <path d="M 0 306 L 545 306 L 545 140 L 380 140 L 250 306 Z" fill="#000"/>
    <rect x="-58" y="-58" width="116" height="116" rx="12" transform="translate(165 5) rotate(45)" fill="#000"/>
    <rect x="-58" y="-58" width="116" height="116" rx="12" transform="translate(80 298) rotate(45)" fill="#000"/>
    <rect role="img" aria-label="Photo: offshore drilling rig at sunset" x="-58" y="-58" width="116" height="116" rx="12" transform="translate(80 95) rotate(45)" fill="url(#g-sunset2)"/>
    <rect role="img" aria-label="Photo: drilling platform lit by low sun" x="-58" y="-58" width="116" height="116" rx="12" transform="translate(250 95) rotate(45)" fill="url(#g-sunset2)"/>
    <rect role="img" aria-label="Photo: pumpjacks in a hazy oil field" x="-58" y="-58" width="116" height="116" rx="12" transform="translate(165 198) rotate(45)" fill="url(#g-field2)"/>
    <rect role="img" aria-label="Photo: refinery towers" x="-58" y="-58" width="116" height="116" rx="12" transform="translate(460 92) rotate(45)" fill="url(#g-rust2)"/>
  </svg>
  <div class="cover-brand brand-name" style="color:#fff"><i></i>HALDEN RIDGE</div>
  <div class="cover-tagline">Consolidating profitable conventional<br>West Texas Oil &amp; Gas wells<br>into a high return investment fund</div>
</section>

<!-- Industry today -->
<section class="slide col-left row-2">
  <div class="notch"></div>
  <h2 class="slide-title">The Industry Today</h2>
  <div class="mini-brand">HALDEN</div>
  <p class="intro">Typical “Major” O&amp;G Companies have thousands of horizontal wells and thousands of vertical wells.<br>They want to focus on horizontal.</p>
  <div class="placeholder" role="img" aria-label="Three oil derrick icons" style="left:72px;top:108px;width:132px;height:58px;background:#2a2a2a;border-radius:3px"></div>
  <div class="placeholder" role="img" aria-label="Ten small oil derrick icons in two rows" style="left:296px;top:106px;width:140px;height:62px;background:#2a2a2a;border-radius:3px"></div>
  <svg class="bg" width="545" height="306" viewBox="0 0 545 306">
    <path d="M134 184 l6 6 l6 -6 v8 l-6 6 l-6 -6 Z" fill="#000"/>
    <path d="M362 184 l6 6 l6 -6 v8 l-6 6 l-6 -6 Z" fill="#000"/>
  </svg>
  <div class="placeholder" role="img" aria-label="Three large oil barrel icons" style="left:80px;top:214px;width:114px;height:62px;background:#2a2a2a;border-radius:3px"></div>
  <div class="placeholder" role="img" aria-label="Eight small oil barrel icons in a row" style="left:296px;top:210px;width:146px;height:28px;background:#2a2a2a;border-radius:3px"></div>
  <div class="callout">Strong economic motivation to divest Vertical wells on<br>good terms to trusted operators like Halden Ridge/HRP.</div>
  <div class="footer-rule"></div>
  <div class="page-no"><span>3</span></div>
</section>

<!-- Interior text -->
<section class="slide col-right row-2">
  <div class="notch"></div>
  <h2 class="slide-title">Title here</h2>
  <div class="mini-brand">HALDEN</div>
  <div class="body-copy" style="left:34px;top:60px;width:470px">
    <p>Lorem ipsum dolor sit amet, consectetuer adipiscing elit. Maecenas porttitor congue massa. Fusce posuere, magna sed pulvinar ultricies, purus lectus malesuada libero, sit amet commodo magna eros quis urna.</p>
    <p>Nunc viverra imperdiet enim. Fusce est. Vivamus a tellus.</p>
    <p class="tight">Pellentesque habitant morbi tristique senectus et netus et malesuada fames ac turpis egestas. Proin pharetra nonummy pede. Mauris et orci.</p>
    <p>Lorem ipsum dolor sit amet, consectetuer adipiscing elit. Maecenas porttitor congue massa. Fusce posuere, magna sed pulvinar ultricies, purus lectus malesuada libero, sit amet commodo magna eros quis urna.</p>
    <p>Nunc viverra imperdiet enim. Fusce est. Vivamus a tellus.</p>
    <p>Pellentesque habitant morbi tristique senectus et netus et malesuada fames ac turpis egestas. Proin pharetra nonummy pede. Mauris et orci.</p>
  </div>
  <div class="footer-rule"></div>
  <div class="page-no"><span>4</span></div>
</section>

<!-- Two column -->
<section class="slide col-left row-3">
  <div class="notch"></div>
  <div class="mini-brand">HALDEN</div>
  <div class="body-copy" style="left:34px;top:60px;width:220px">
    <p>Lorem ipsum dolor sit amet, consectetuer adipiscing elit. Maecenas porttitor congue massa. Fusce posuere, magna sed pulvinar ultricies, purus lectus malesuada libero, sit amet commodo magna eros quis urna.</p>
    <p>Nunc viverra imperdiet enim. Fusce est. Vivamus a tellus.</p>
    <p class="tight">Pellentesque habitant morbi tristique senectus et netus et malesuada fames ac turpis egestas. Proin pharetra nonummy pede. Mauris et orci.</p>
    <p>Lorem ipsum dolor sit amet, consectetuer adipiscing elit. Maecenas porttitor congue massa. Fusce posuere, magna sed pulvinar ultricies, purus lectus malesuada libero, sit amet commodo magna eros quis urna.</p>
  </div>
  <div class="body-copy" style="left:277px;top:60px;width:235px">
    <p>Lorem ipsum dolor sit amet, consectetuer adipiscing elit. Maecenas porttitor congue massa. Fusce posuere, magna sed pulvinar ultricies, purus lectus malesuada libero, sit amet commodo magna eros quis urna.</p>
    <p>Nunc viverra imperdiet enim. Fusce est. Vivamus a tellus.</p>
    <p class="tight">Pellentesque habitant morbi tristique senectus et netus et malesuada fames ac turpis egestas. Proin pharetra nonummy pede. Mauris et orci.</p>
    <p>Lorem ipsum dolor sit amet, consectetuer adipiscing elit. Maecenas porttitor congue massa. Fusce posuere, magna sed pulvinar ultricies, purus lectus malesuada libero, sit amet commodo magna eros quis urna.</p>
  </div>
  <div class="footer-rule"></div>
  <div class="page-no"><span>5</span></div>
</section>

<!-- Text with photo -->
<section class="slide col-right row-3">
  <div class="notch"></div>
  <h2 class="slide-title">Title here</h2>
  <div class="mini-brand">HALDEN</div>
  <div class="body-copy" style="left:34px;top:60px;width:222px">
    <p>Lorem ipsum dolor sit amet, consectetuer adipiscing elit. Maecenas porttitor congue massa. Fusce posuere, magna sed pulvinar ultricies, purus lectus malesuada libero, sit amet commodo magna eros quis urna.</p>
    <p>Nunc viverra imperdiet enim. Fusce est. Vivamus a tellus.</p>
    <p class="tight">Pellentesque habitant morbi tristique senectus et netus et malesuada fames ac turpis egestas. Proin pharetra nonummy pede. Mauris et orci.</p>
    <p>Lorem ipsum dolor sit amet, consectetuer adipiscing elit. Maecenas porttitor congue massa. Fusce posuere, magna sed pulvinar ultricies, purus lectus malesuada libero, sit amet commodo magna eros quis urna.</p>
  </div>
  <div class="footer-rule"></div>
  <div class="placeholder" role="img" aria-label="Photo: pumpjack silhouetted against an amber sky" style="left:273px;top:0;width:208px;height:306px;background:linear-gradient(160deg,var(--photo-amber-a),var(--photo-amber-b))"></div>
  <div class="page-no"><span>6</span></div>
</section>

<!-- Team -->
<section class="slide col-left row-4">
  <div class="notch"></div>
  <h2 class="slide-title">Team</h2>
  <div class="mini-brand">HALDEN</div>
  <div class="advisors-label">ADVISORS</div>
  <div class="team-divider"></div>
  <svg class="bg" width="545" height="306" viewBox="0 0 545 306">
    <defs><linearGradient id="g-portrait" x1="0" y1="0" x2="0" y2="1"><stop offset="0" stop-color="var(--portrait-a)"/><stop offset="1" stop-color="var(--portrait-b)"/></linearGradient></defs>
    <rect role="img" aria-label="Portrait of Alan Mercer" x="52" y="67" width="56" height="56" rx="8" transform="rotate(45 80 95)" fill="url(#g-portrait)"/>
    <rect role="img" aria-label="Portrait of Daniel Foster" x="140" y="67" width="56" height="56" rx="8" transform="rotate(45 168 95)" fill="url(#g-portrait)"/>
    <rect role="img" aria-label="Portrait of Craig Holloway" x="237" y="67" width="56" height="56" rx="8" transform="rotate(45 265 95)" fill="url(#g-portrait)"/>
    <rect role="img" aria-label="Portrait of Warren Pike" x="342" y="67" width="56" height="56" rx="8" transform="rotate(45 370 95)" fill="url(#g-portrait)"/>
    <rect role="img" aria-label="Portrait of Martin Hale" x="440" y="67" width="56" height="56" rx="8" transform="rotate(45 468 95)" fill="url(#g-portrait)"/>
  </svg>
  <div class="team-member" style="left:80px"><div class="name">Alan Mercer</div><div class="role">Managing Partner + CEO, Halvern Resources</div><div class="bio">Extensive oilfield operations leadership, including VP &amp; GM roles at a large producer responsible for 1000+ horizontal and 6000+ vertical wells.</div></div>
  <div class="team-member" style="left:168px"><div class="name">Daniel Foster</div><div class="role">Managing Partner, Halden Ridge</div><div class="bio">Broad P&amp;L and management experience, including positions at a global electronic materials company.</div></div>
  <div class="team-member" style="left:265px"><div class="name">Craig Holloway</div><div class="role">Operations Manager</div><div class="bio">Over 40 years of oilfield experience in operations, drilling and equipment maintenance. Oversees daily field operations and production.</div></div>
  <div class="team-member" style="left:370px"><div class="name">Warren Pike, P.E.</div><div class="bio">Over 18 years of experience in Permian Basin oil and gas operations, including engineering, field and executive roles.</div></div>
  <div class="team-member" style="left:468px"><div class="name">Martin Hale</div><div class="role">Reserves Analysis and Property Evaluation</div><div class="bio">Registered Petroleum Engineer with 30+ years of experience and deep background in the Permian Basin.</div></div>
  <div class="partner-strip">
    <span class="partner-badge"></span><span class="partner-badge"></span><span class="partner-badge"></span><span class="partner-badge"></span><span class="partner-badge"></span>
  </div>
  <div class="footer-rule"></div>
  <div class="page-no"><span>7</span></div>
</section>

<!-- Disclaimer -->
<section class="slide col-right row-4">
  <div class="notch"></div>
  <h2 class="slide-title">Disclaimer</h2>
  <div class="mini-brand">HALDEN</div>
  <div class="disclaimer-band">Nothing contained in these documents and materials is meant to be, and shall not be considered, a security offering, an offer to invest, or a solicitation of funds for any purpose. All information contained in these materials and documents, including, but not limited to, numbers, dollar amounts, rates of return, oil production, projections, etc. are included in such materials and documents purely for informational and discussion purposes only, and are strictly conjecture. The success of this proposed business idea or venture is not guaranteed in any way, and any investment in such business idea or venture carries the risk of significant or complete loss of investment.</div>
  <div class="footer-rule"></div>
  <div class="page-no"><span>8</span></div>
</section>

<!-- Thank you, light -->
<section class="slide col-left row-5" style="color:var(--ink)">
  <svg class="bg" width="545" height="306" viewBox="0 0 545 306">
    <defs><linearGradient id="g-refinery" x1="0" y1="0" x2="1" y2="1"><stop offset="0" stop-color="var(--photo-rust-a)"/><stop offset="1" stop-color="var(--photo-rust-b)"/></linearGradient></defs>
    <path role="img" aria-label="Photo: refinery columns at dusk" d="M240 0 H545 V306 H415 L180 110 Q165 95 180 80 Z" fill="url(#g-refinery)"/>
  </svg>
  <div class="thanks-rule"></div>
  <div class="thanks-brand brand-name"><i></i>HALDEN RIDGE</div>
  <div class="thanks-title">Thank You</div>
  <div class="thanks-copy">Lorem ipsum dolor sit amet, consectetuer adipiscing elit. Maecenas porttitor congue massa. Fusce</div>
  <div class="social"><span></span><span></span><span></span></div>
</section>

<!-- Thank you, dark -->
<section class="slide slide--dark col-right row-5">
  <svg class="bg" width="545" height="306" viewBox="0 0 545 306">
    <defs><linearGradient id="g-refinery2" x1="0" y1="0" x2="1" y2="1"><stop offset="0" stop-color="var(--photo-rust-a)"/><stop offset="1" stop-color="var(--photo-rust-b)"/></linearGradient></defs>
    <path role="img" aria-label="Photo: refinery columns at dusk" d="M240 0 H545 V306 H415 L180 110 Q165 95 180 80 Z" fill="url(#g-refinery2)"/>
  </svg>
  <div class="thanks-brand brand-name"><i></i>HALDEN RIDGE</div>
  <div class="thanks-title">Thank You</div>
  <div class="thanks-copy">Lorem ipsum dolor sit amet, consectetuer adipiscing elit. Maecenas porttitor congue massa. Fusce</div>
  <div class="social"><span></span><span></span><span></span></div>
</section>

</body>
</html>
```